Creative Card Game Card Design for a Unique Universe

We are designing a physical card game whose closest cousin is "Sorcery: The Convergence" (http://www.quellbright.example/Sorcery). We are in need of a CREATIVE design for the cards that is similar, but different and unique, compared to other card games. Card designs should fit within the fantasy realm, but ultimately be portable to other genres, such as science fiction or medieval.

The fundamentals of our cards include:
• Title (up to ~3 long-ish words)
• Card type icon (attack, defend, augmented attack, augmented defend)
• Image (majority of the card)
• Instructional text area 1 (up to ~25 words)
• Instructional text area 2 (up to ~30 words)
• Copyright area
• Game logo area

The back of the card identifies each type of card with a different background with the game logo and title in front of it (probably white). Current ideas for backgrounds identifying the different types of cards are fiery red, metallic silver, marble green, and brown leather, so feel free to suggest textures for those as well.

Areas where we are looking for creativity:
• Textures and backgrounds (e.g. we like the parchment/antique paper look)
• Interesting use of transparency and/or gradient colors
• Shape and positioning of elements (but still needs to be functional)
• Overlapping of elements
• Card borders (if they make sense in your design)
• Icon style
• Fonts (we use "Lindsay EF" in our manual)
• Card size (but still needs to be usable in the player's hand; standard size is ~2.5" x 3.5")
• Card shape (but still needs to be usable in the player's hand; e.g. Rectangular but with a rounded corner)

Restrictions on the design:
• Design should be in color
• Card shape can be creative (but not too "out there"), but should be a reasonable cost to print
• First priority is to print, but cards will also be used in an iPad app

Tools:
• We would prefer the design was submitted in Adobe Illustrator format (vector-based)

We will give extra attention to designs that are truly unique and that we haven't seen before!

For examples of Sorcery cards, see http://www.quellbright.example/sorcery/tcg/article.aspx?x=stc/tcg/sorcery2013/cig

Thank you!
Updates

Hi there,

Appreciate you thinking about our little card design project! Just wanted to provide an update that I uploaded another file (a logo) on request, and also updated the comments with some sample text for a card, also on request.

Thanks,

Oliver.

Project Deadline Extended
Reason: Our small team isn't meeting until Wed to discuss the designs, so extending until we've had a chance to discuss the designs. Thanks, Oliver.

Target Market(s)

Teenagers+, English-speaking to start

Industry/Entity Type

Games

Font styles to use
Other font styles liked:
• Lindsay EF

Colors

Designer to choose colors to be used in the design.

Requirements
Should not have
• An identical look to other card games, like Sorcery.

```html
<!DOCTYPE html>
<html lang="en">
<head>
<meta charset="utf-8">
<title>Swing – Card</title>
<link rel="stylesheet" href="https://fonts.googleapis.com/css2?family=MedievalSharp&family=Open+Sans&display=swap">
<style>
  :root {
    --ink: #000;
    --parchment-light: #f4c766;
    --parchment-mid: #e3a53e;
    --parchment-dark: #b87a26;
    --frame-line: #2e220e;
    --oval-top: #ebe6d8;
    --oval-haze: #c9c0a8;
    --oval-mid: #7a6743;
    --oval-bottom: #33271a;
    --title: #dcd9c8;
    --label: #eea64a;
    --body: #ebe5d2;
    --token-red: #a8271b;
    --token-parchment: #e6c58a;
    --copyright: #8a8a8a;
  }
  html, body { margin: 0; padding: 0; background: var(--ink); overflow: hidden; }
  .card {
    position: relative; width: 773px; height: 1200px; overflow: hidden;
    background: var(--ink);
  }
  .card-art { position: absolute; inset: 0; }
  .card-title {
    position: absolute; left: 0; width: 773px; top: 560px; margin: 0;
    text-align: center; font-family: "MedievalSharp", serif; font-weight: 400;
    font-size: 124px; line-height: 1; color: var(--title);
    text-shadow: 3px 4px 5px rgba(0,0,0,.75);
  }
  .card-rules {
    position: absolute; left: 174px; top: 718px; width: 480px; margin: 0;
    font-family: "MedievalSharp", serif; font-size: 28px; line-height: 49px;
    color: var(--body); text-shadow: 1px 2px 2px rgba(0,0,0,.85);
    white-space: nowrap;
  }
  .card-rules .label { color: var(--label); }
  .card-copyright {
    position: absolute; left: 0; width: 773px; top: 1151px; margin: 0;
    text-align: center; font-family: "Open Sans", sans-serif; font-size: 13px;
    color: var(--copyright);
  }
</style>
</head>
<body>
<div class="card">
  <svg class="card-art" width="773" height="1200" viewBox="0 0 773 1200">
    <defs>
      <linearGradient id="parchment" x1="0" y1="0" x2="1" y2="1">
        <stop offset="0" stop-color="var(--parchment-mid)"/>
        <stop offset=".5" stop-color="var(--parchment-light)"/>
        <stop offset="1" stop-color="var(--parchment-mid)"/>
      </linearGradient>
      <radialGradient id="stain" cx=".5" cy=".5" r=".5">
        <stop offset="0" stop-color="var(--parchment-dark)" stop-opacity=".55"/>
        <stop offset="1" stop-color="var(--parchment-dark)" stop-opacity="0"/>
      </radialGradient>
      <radialGradient id="glow" cx=".5" cy=".5" r=".5">
        <stop offset="0" stop-color="#fbe3a0" stop-opacity=".7"/>
        <stop offset="1" stop-color="#fbe3a0" stop-opacity="0"/>
      </radialGradient>
      <linearGradient id="oval-fill" x1="0" y1="0" x2="0" y2="1">
        <stop offset="0" stop-color="var(--oval-top)"/>
        <stop offset=".35" stop-color="#ddd6c4"/>
        <stop offset=".45" stop-color="var(--oval-haze)"/>
        <stop offset=".56" stop-color="var(--oval-mid)"/>
        <stop offset=".7" stop-color="#4e3e27"/>
        <stop offset="1" stop-color="var(--oval-bottom)"/>
      </linearGradient>
      <radialGradient id="hero-fill" cx=".5" cy=".45" r=".5">
        <stop offset="0" stop-color="#9a6446" stop-opacity=".6"/>
        <stop offset=".55" stop-color="#a78466" stop-opacity=".35"/>
        <stop offset="1" stop-color="#c9bba0" stop-opacity="0"/>
      </radialGradient>
      <radialGradient id="vignette" cx=".5" cy=".5" r=".5">
        <stop offset=".8" stop-color="#000" stop-opacity="0"/>
        <stop offset="1" stop-color="#2a1d0c" stop-opacity=".45"/>
      </radialGradient>
      <clipPath id="oval-clip"><ellipse cx="388" cy="594" rx="335" ry="541"/></clipPath>
      <clipPath id="frame-clip"><rect x="42" y="48" width="687" height="1089"/></clipPath>
    </defs>

    <g class="card-frame" clip-path="url(#frame-clip)">
      <rect x="42" y="48" width="687" height="1089" fill="url(#parchment)"/>
      <ellipse cx="90" cy="300" rx="90" ry="160" fill="url(#stain)"/>
      <ellipse cx="700" cy="280" rx="80" ry="150" fill="url(#stain)"/>
      <ellipse cx="80" cy="820" rx="70" ry="180" fill="url(#stain)"/>
      <ellipse cx="710" cy="860" rx="70" ry="170" fill="url(#stain)"/>
      <ellipse cx="90" cy="560" rx="60" ry="120" fill="url(#glow)"/>
      <ellipse cx="690" cy="580" rx="60" ry="120" fill="url(#glow)"/>
    </g>
    <rect x="42" y="48" width="687" height="1089" fill="none" stroke="var(--frame-line)" stroke-width="3"/>
    <rect x="48" y="54" width="675" height="1077" fill="none" stroke="#7a5a24" stroke-width="1.5"/>

    <ellipse class="card-oval" cx="388" cy="594" rx="335" ry="541" fill="url(#oval-fill)"/>
    <g clip-path="url(#oval-clip)">
      <ellipse class="card-illustration" role="img" aria-label="Illustration of an armoured warrior drawing a curved bow" cx="400" cy="330" rx="260" ry="300" fill="url(#hero-fill)"/>
      <ellipse cx="388" cy="594" rx="335" ry="541" fill="url(#vignette)"/>
    </g>
    <ellipse cx="388" cy="594" rx="335" ry="541" fill="none" stroke="var(--frame-line)" stroke-width="4"/>
    <ellipse cx="388" cy="594" rx="340" ry="546" fill="none" stroke="#8a6a30" stroke-width="2"/>

    <g class="type-token type-token--attack">
      <circle cx="114" cy="105" r="70" fill="var(--token-parchment)" stroke="#5a4226" stroke-width="5"/>
      <circle cx="114" cy="105" r="62" fill="none" stroke="#8a6a3a" stroke-width="1.5"/>
      <path d="M92 84 L146 146" stroke="#8a1f16" stroke-width="8" stroke-linecap="round"/>
      <path d="M74 82 Q100 64 124 84 L110 100 Q98 88 80 96 Z" fill="#a3241a"/>
    </g>
    <g class="type-token type-token--defend">
      <circle cx="655" cy="123" r="70" fill="var(--token-red)" stroke="#3a1a10" stroke-width="5"/>
      <circle cx="655" cy="123" r="62" fill="none" stroke="#d08a5a" stroke-width="1.5" opacity=".6"/>
      <path d="M617 85 L693 161 M693 85 L617 161" stroke="#e9d9b0" stroke-width="5" stroke-linecap="round"/>
      <path d="M625 145 L637 157 M685 145 L673 157" stroke="#e9d9b0" stroke-width="9" stroke-linecap="round"/>
    </g>
    <g class="type-token type-token--augment">
      <circle cx="116" cy="1063" r="70" fill="var(--token-red)" stroke="#3a1a10" stroke-width="5"/>
      <circle cx="116" cy="1063" r="62" fill="none" stroke="#d08a5a" stroke-width="1.5" opacity=".6"/>
      <path d="M94 1027 H138 Q138 1067 116 1071 Q94 1067 94 1027 Z" fill="#d8d0bf"/>
      <path d="M116 1071 V1099 M100 1103 H132" stroke="#d8d0bf" stroke-width="6" stroke-linecap="round"/>
    </g>
    <g class="type-token type-token--target">
      <circle cx="656" cy="1065" r="70" fill="var(--token-parchment)" stroke="#5a4226" stroke-width="5"/>
      <circle cx="656" cy="1065" r="62" fill="none" stroke="#8a6a3a" stroke-width="1.5"/>
      <circle cx="656" cy="1065" r="34" fill="none" stroke="#5a4a35" stroke-width="4"/>
      <circle cx="656" cy="1065" r="14" fill="none" stroke="#5a4a35" stroke-width="3"/>
      <path d="M656 1019 V1111 M610 1065 H702" stroke="#5a4a35" stroke-width="3"/>
    </g>
  </svg>

  <h1 class="card-title">Swing</h1>
  <p class="card-rules">
    <span class="label">Requirement:</span> None<br>
    <span class="label">Optional Cost:</span> Any attack card<br>
    or any 2 cards for +1 damage; or<br>
    additional SWING card for +2<br>
    <span class="label">Effect:</span> SWING damage
  </p>
  <p class="card-copyright">©Copyright 2014&nbsp; Game Name&nbsp; All Rights Reserved.</p>
</div>
</body>
</html>
```